BRAVEN VOLTWORKS SERVICES needs a vibrant design for electrical contracting work.

I require a card design for my own electrical contracting business. I will be doing a lot of domestic and commercial work, including things such as repairs, maintenance, lighting, installations and various others. LED lighting and energy efficiency will be a big part of my business. I wish not to have childish pictures such as light bulbs in the design, but rather a smart and modern looking card which incorporates my logo colours and perhaps the same lighting strike within the faded background of the card.

Target Market(s)

Residential and Commercial property owners.

Industry/Entity Type

Electrical

Contact Information for Business Card

Dario Pesek
EC40362
Phone Number: 0417 538 924
Email: dario@bravenvoltworks.com

Font styles to use
Serif
Sans Serif

Requirements
Must have
• My Logo and associated colours.
Nice to have
• Some form of shapes splitting the card into different colours related to the colours of my logo. Electric Blue, Silver/Grey and White.
Should not have
• Childish pictures and symbols such as light bulbs.

```html
<!DOCTYPE html>
<html lang="en">
<head>
<meta charset="utf-8">
<title>Braven Voltworks Services – Business Cards</title>
<link rel="stylesheet" href="https://fonts.googleapis.com/css2?family=Orbitron:wght@500;700&display=swap">
<style>
  :root {
    --electric-blue: #1010f0;
    --blue-soft: #3434f4;
    --ink: #151515;
    --paper: #ffffff;
    --silver: #9a9ca0;
    --ghost-light: #eef0f0;
    --ghost-dark: #3c3e3e;
  }
  html, body {
    margin: 0;
    width: 1200px;
    height: 900px;
    overflow: hidden;
    background: var(--paper);
    font-family: "Orbitron", sans-serif;
  }
  .sheet { position: relative; width: 1200px; height: 900px; }
  .card {
    position: absolute;
    width: 452px;
    height: 264px;
    box-shadow: 4px 6px 8px rgba(0,0,0,0.35);
    overflow: hidden;
  }
  .card--blue-white { left: 129px; top: 163px; }
  .card--black-blue { left: 626px; top: 163px; }
  .card--black-white { left: 129px; top: 483px; }
  .card--all-black { left: 626px; top: 483px; }
  .card__bg { position: absolute; inset: 0; }
  .brand {
    position: absolute;
    left: 26px;
    top: 36px;
    display: flex;
    align-items: center;
    gap: 10px;
  }
  .brand__dot {
    width: 46px; height: 46px;
    border-radius: 50%;
    background: var(--electric-blue);
  }
  .brand__name {
    font-weight: 700;
    font-size: 17px;
    line-height: 1.15;
    letter-spacing: 0.5px;
    color: var(--electric-blue);
  }
  .card--black-white .brand__name,
  .card--black-blue .brand__name,
  .card--all-black .brand__name { color: var(--silver); }
  .contact {
    position: absolute;
    left: 51px;
    top: 170px;
    color: var(--paper);
  }
  .contact__name {
    font-size: 17px;
    font-weight: 500;
    letter-spacing: 0.8px;
    margin: 0 0 10px;
  }
  .contact__row {
    display: flex;
    align-items: center;
    gap: 12px;
    font-size: 11.5px;
    letter-spacing: 0.6px;
    margin-bottom: 7px;
  }
  .contact__row svg { width: 17px; height: 12px; fill: currentColor; }
  .card--black-white .contact { color: var(--ink); }
  .card--all-black .contact { color: var(--electric-blue); }
</style>
</head>
<body>
<main class="sheet">

  <!-- Blue frame, white top, blue lower band -->
  <section class="card card--blue-white">
    <svg class="card__bg" viewBox="0 0 452 264" aria-hidden="true">
      <rect width="452" height="264" fill="var(--electric-blue)"/>
      <rect x="8" y="8" width="436" height="248" fill="var(--paper)"/>
      <polygon points="8,158 444,91 444,256 8,256" fill="var(--electric-blue)"/>
      <clipPath id="c1"><rect x="8" y="8" width="436" height="248"/></clipPath>
      <circle cx="382" cy="200" r="82" fill="var(--blue-soft)" clip-path="url(#c1)"/>
    </svg>
    <div class="brand"><span class="brand__dot"></span><span class="brand__name">BRAVEN VOLTWORKS<br>SERVICES</span></div>
    <div class="contact">
      <p class="contact__name">Dario Pesek EC40362</p>
      <div class="contact__row"><svg viewBox="0 0 17 12"><path d="M1 4C1 1 16 1 16 4L13 5 12 3H5L4 5ZM4 6H13L15 12H2Z"/></svg>0417 538 924</div>
      <div class="contact__row"><svg viewBox="0 0 17 12"><path d="M1 1H16V11H1ZM2 2.5V3L8.5 7 15 3V2.5Z"/></svg>dario@bravenvoltworks.com</div>
    </div>
  </section>

  <!-- White frame, black top, blue lower band with white rule -->
  <section class="card card--black-blue">
    <svg class="card__bg" viewBox="0 0 452 264" aria-hidden="true">
      <rect width="452" height="264" fill="var(--paper)"/>
      <rect x="8" y="8" width="436" height="248" fill="var(--ink)"/>
      <polygon points="8,158 444,91 444,256 8,256" fill="var(--paper)"/>
      <polygon points="8,162 444,95 444,256 8,256" fill="var(--electric-blue)"/>
      <clipPath id="c2"><rect x="8" y="8" width="436" height="248"/></clipPath>
      <circle cx="382" cy="200" r="82" fill="var(--blue-soft)" clip-path="url(#c2)"/>
      <rect x="8" y="8" width="436" height="248" fill="none"/>
    </svg>
    <div class="brand"><span class="brand__dot"></span><span class="brand__name">BRAVEN VOLTWORKS<br>SERVICES</span></div>
    <div class="contact">
      <p class="contact__name">Dario Pesek EC40362</p>
      <div class="contact__row"><svg viewBox="0 0 17 12"><path d="M1 4C1 1 16 1 16 4L13 5 12 3H5L4 5ZM4 6H13L15 12H2Z"/></svg>0417 538 924</div>
      <div class="contact__row"><svg viewBox="0 0 17 12"><path d="M1 1H16V11H1ZM2 2.5V3L8.5 7 15 3V2.5Z"/></svg>dario@bravenvoltworks.com</div>
    </div>
  </section>

  <!-- White frame, black top, white lower area -->
  <section class="card card--black-white">
    <svg class="card__bg" viewBox="0 0 452 264" aria-hidden="true">
      <rect width="452" height="264" fill="var(--paper)"/>
      <polygon points="8,8 444,8 444,91 8,155" fill="var(--ink)"/>
      <clipPath id="c3"><polygon points="8,155 444,91 444,256 8,256"/></clipPath>
      <circle cx="382" cy="200" r="82" fill="var(--ghost-light)" clip-path="url(#c3)"/>
    </svg>
    <div class="brand"><span class="brand__dot"></span><span class="brand__name">BRAVEN VOLTWORKS<br>SERVICES</span></div>
    <div class="contact">
      <p class="contact__name">Dario Pesek EC40362</p>
      <div class="contact__row"><svg viewBox="0 0 17 12"><path d="M1 4C1 1 16 1 16 4L13 5 12 3H5L4 5ZM4 6H13L15 12H2Z"/></svg>0417 538 924</div>
      <div class="contact__row"><svg viewBox="0 0 17 12"><path d="M1 1H16V11H1ZM2 2.5V3L8.5 7 15 3V2.5Z"/></svg>dario@bravenvoltworks.com</div>
    </div>
  </section>

  <!-- Blue frame, all black -->
  <section class="card card--all-black">
    <svg class="card__bg" viewBox="0 0 452 264" aria-hidden="true">
      <rect width="452" height="264" fill="var(--electric-blue)"/>
      <rect x="8" y="8" width="436" height="248" fill="var(--ink)"/>
      <clipPath id="c4"><rect x="8" y="8" width="436" height="248"/></clipPath>
      <circle cx="382" cy="200" r="82" fill="var(--ghost-dark)" clip-path="url(#c4)"/>
    </svg>
    <div class="brand"><span class="brand__dot"></span><span class="brand__name">BRAVEN VOLTWORKS<br>SERVICES</span></div>
    <div class="contact">
      <p class="contact__name">Dario Pesek EC40362</p>
      <div class="contact__row"><svg viewBox="0 0 17 12"><path d="M1 4C1 1 16 1 16 4L13 5 12 3H5L4 5ZM4 6H13L15 12H2Z"/></svg>0417 538 924</div>
      <div class="contact__row"><svg viewBox="0 0 17 12"><path d="M1 1H16V11H1ZM2 2.5V3L8.5 7 15 3V2.5Z"/></svg>dario@bravenvoltworks.com</div>
    </div>
  </section>

</main>
</body>
</html>
```